Building company with a modern and unique product looking for a business card to help us stand out

We currently have a logo but as our business has grown, we feel that our business card is not reflecting our modern and high quality product and help us stand out from the crowd. Our business is mainly in the construction of new homes using a unique method and materials that makes our homes fire proof, vermin and pest resistant and rated to the maximum cyclone category (category 5). We need a business card that helps us stand out as well as communicating professionalism, high quality and trustworthiness. I have attached our current logo with a black and white option, as well as our business card which is double sided. We would like to retain as much of the information that is currently on our business cards, but presented in a more sleek way. We do like our current colour palette ( white, black, yellow and grey) and have been looking primarily at business cards with a black background however we are open to other combinations of colour and layout as long as we stand out. Please feel free to tweak our logo to make it more suitable for a business card, we like the black option that we use but we have had trouble trying to get the white area to match the rest of the logo and blend effectively into a business card. Please do not hesitate to contact us with any questions as we really want this to be successful!

Target Market(s)

Large contracts including government and larger companies

Industry/Entity Type

Business

We will be providing this business card to potential clients including key government ministers and large funding companies, our business card should show that we are professional and reliable.

Requirements
Must have
• It must be easy to read and pleasing to the eye, It must contain as much of the information on the current business card and unless something really stands out, we will most likely pick a design that has all of the information included. It must include our logo of course and have some colour included.
Nice to have
• We are looking for a high end business card and would like to see designs that reflect this. We like the gloss/matte contrast, plastic cards with opaque/coloured areas and unique features not seen on everyday paper business cards. It would be nice to see a few different colour combinations, we are open to new ideas so please feel free to take some artistic licence.
Should not have
• Must not be too busy, difficult to read or be distracting from the information conveyed. Other than this please feel free to add your own touches and make it unique!

```html
<!DOCTYPE html>
<html lang="en">
<head>
<meta charset="utf-8">
<title>Halden Building Company – Business Card</title>
<link rel="stylesheet" href="https://fonts.googleapis.com/css2?family=Tinos:wght@400;700&family=Open+Sans:wght@400;600&display=swap">
<style>
  :root {
    --gold: #c9a52a;
    --gold-soft: #d4b23a;
    --black: #0b0b0b;
    --white: #ffffff;
    --grey: #5a5a5a;
    --ink: #222222;
    --backdrop: #e9e6df;
  }
  * { box-sizing: border-box; margin: 0; padding: 0; }
  html, body { width: 1200px; height: 900px; overflow: hidden; }
  body {
    background: var(--backdrop);
    display: flex;
    align-items: center;
    justify-content: center;
    gap: 40px;
    font-family: "Open Sans", Arial, sans-serif;
  }
  .card {
    position: relative;
    width: 520px;
    height: 297px;
    overflow: hidden;
    box-shadow: 0 6px 18px rgba(0,0,0,0.18);
  }

  /* Front */
  .card-front {
    background: var(--black);
    display: flex;
    align-items: center;
    justify-content: center;
  }
  .brand {
    display: flex;
    align-items: center;
    gap: 12px;
    font-family: "Tinos", "Times New Roman", serif;
    font-weight: 400;
  }
  .brand-mark {
    width: 14px;
    height: 14px;
    background: var(--gold);
    flex: none;
  }
  .card-front .brand-name {
    color: var(--white);
    font-size: 38px;
    line-height: 1.05;
    text-align: center;
  }

  /* Back */
  .card-back { background: var(--white); }
  .card-back .shapes { position: absolute; inset: 0; }
  .card-back .brand {
    position: absolute;
    left: 34px;
    top: 40px;
    gap: 9px;
  }
  .card-back .brand-mark { width: 10px; height: 10px; }
  .card-back .brand-name {
    color: var(--ink);
    font-size: 21px;
    line-height: 1.05;
  }
  .holder {
    position: absolute;
    left: 40px;
    top: 148px;
    color: var(--white);
  }
  .holder-name {
    font-family: "Tinos", "Times New Roman", serif;
    font-weight: 700;
    font-size: 21px;
    letter-spacing: 0.3px;
  }
  .holder-role {
    font-size: 12.5px;
    margin-top: 1px;
  }
  .contacts {
    position: absolute;
    right: 22px;
    top: 182px;
    list-style: none;
    display: flex;
    flex-direction: column;
    gap: 6px;
  }
  .contacts li {
    display: flex;
    align-items: center;
    justify-content: flex-end;
    gap: 8px;
    font-size: 12.5px;
    color: var(--ink);
    letter-spacing: 0.3px;
  }
  .contact-icon {
    width: 16px;
    height: 16px;
    flex: none;
  }
</style>
</head>
<body>

  <section class="card card-front" aria-label="Card front">
    <div class="brand">
      <span class="brand-mark"></span>
      <span class="brand-name">Halden Building<br>Company</span>
    </div>
  </section>

  <section class="card card-back" aria-label="Card back">
    <svg class="shapes" viewBox="0 0 520 297" width="520" height="297" aria-hidden="true">
      <rect x="0" y="0" width="520" height="16" fill="var(--gold)"/>
      <polygon points="300,16 520,16 520,136 340,136" fill="var(--gold-soft)"/>
      <polyline points="288,16 332,146 520,146" fill="none" stroke="var(--gold)" stroke-width="2.5"/>
      <polygon points="0,122 232,122 282,297 0,297" fill="var(--black)"/>
      <polyline points="0,129 227,129 274,297" fill="none" stroke="var(--white)" stroke-width="2"/>
      <rect x="0" y="276" width="520" height="21" fill="var(--black)"/>
    </svg>

    <div class="brand">
      <span class="brand-mark"></span>
      <span class="brand-name">Halden Building<br>Company</span>
    </div>

    <div class="holder">
      <p class="holder-name">Marcus Keller</p>
      <p class="holder-role">Managing Director</p>
    </div>

    <ul class="contacts">
      <li>0400 555 123
        <svg class="contact-icon" viewBox="0 0 16 16" aria-label="Mobile">
          <circle cx="8" cy="8" r="8" fill="var(--grey)"/>
          <rect x="5.5" y="3.5" width="5" height="9" rx="1" fill="var(--white)"/>
        </svg>
      </li>
      <li>(02) 5550 1234
        <svg class="contact-icon" viewBox="0 0 16 16" aria-label="Phone">
          <circle cx="8" cy="8" r="8" fill="var(--grey)"/>
          <path d="M5 4.2c.4-.4 1-.4 1.3 0l.9 1.2c.3.4.2.9-.1 1.2l-.5.5c.5 1 1.3 1.8 2.3 2.3l.5-.5c.3-.3.8-.4 1.2-.1l1.2.9c.4.3.4.9 0 1.3l-.6.6c-.6.6-1.6.7-2.4.2-1.7-1-3.1-2.4-4.1-4.1-.5-.8-.4-1.8.2-2.4z" fill="var(--white)"/>
        </svg>
      </li>
      <li>office@haldenbuild.com
        <svg class="contact-icon" viewBox="0 0 16 16" aria-label="Email">
          <circle cx="8" cy="8" r="8" fill="var(--grey)"/>
          <rect x="4" y="5" width="8" height="6" rx="0.5" fill="var(--white)"/>
          <polyline points="4.3,5.4 8,8.4 11.7,5.4" fill="none" stroke="var(--grey)" stroke-width="0.9"/>
        </svg>
      </li>
    </ul>
  </section>

</body>
</html>
```